rk ironcraft business card metallic look

revamp the existing design but want card to have a metalic look to it

Target Market(s)

construction industry

Industry/Entity Type

constrction

Contact Information for Business Card

front of card RK Ironcraft, phone 4165550193, email rk.ironcraftt@veltrano.com and instagram account; rk_ironcraft_

Font styles to use
Other font styles liked:
• masculine

Colors

Designer to choose only greyscale colors for use in the design.

Requirements
Must have
• back side RK Ironcraft then a list of everything : Siding, ACM Panels, Standing Seam,Soffit, Fascia, Gutters,Metal,Alu,inum, Viynyl, Metal Roofs and roof repairs
Nice to have
• I would like to keep the look of the existing card with the metal grids on the front
Should not have
• Need a design in two days

```html
<!DOCTYPE html>
<html lang="en">
<head>
<meta charset="utf-8">
<title>RK Ironcraft – Business Card</title>
<link rel="stylesheet" href="https://fonts.googleapis.com/css2?family=Poppins:wght@400;600&display=swap">
<style>
  :root {
    --page-bg: #3b3b3b;
    --card-base: #2c2c2b;
    --steel-dark: #1b1b1b;
    --steel-mid: #464646;
    --frame-line: #a9a9a9;
    --text-light: #e4e4e4;
    --mark-grey: #3d3d3d;
    --mark-edge: #5a5a5a;
  }
  * { margin: 0; padding: 0; box-sizing: border-box; }
  html, body { width: 1021px; height: 1200px; overflow: hidden; }
  body {
    background: var(--page-bg);
    font-family: "Poppins", sans-serif;
    color: var(--text-light);
    position: relative;
  }
  .card {
    position: absolute;
    left: 171px;
    width: 679px;
    height: 440px;
    background: var(--card-base);
  }
  .card--front { top: 141px; }
  .card--back { top: 619px; }
  .steel-panel {
    position: absolute;
    left: 9px; top: 9px; right: 9px;
    background: linear-gradient(160deg, var(--steel-dark) 5%, var(--steel-mid) 50%, var(--steel-dark) 80%);
  }
  .card--front .steel-panel { height: 296px; }
  .card--back .steel-panel { bottom: 9px; }
  .frame { position: absolute; inset: 0; width: 679px; height: 440px; }
  .frame line { stroke: var(--frame-line); stroke-width: 0.8; }
  .wordmark {
    position: absolute;
    font-weight: 600;
    color: var(--mark-grey);
    line-height: 1;
    letter-spacing: 2px;
    text-shadow: none;
  }
  .card--front .wordmark-initials { left: 44px; top: 40px; font-size: 172px; }
  .card--front .wordmark-name { left: 46px; top: 222px; font-size: 58px; }
  .card--back .wordmark-initials { left: 34px; top: 24px; font-size: 132px; }
  .card--back .wordmark-name { left: 36px; top: 163px; font-size: 44px; }
  .contact {
    position: absolute;
    display: flex;
    align-items: center;
    gap: 6px;
    font-size: 14px;
    line-height: 1;
  }
  .contact svg { width: 15px; height: 15px; flex: none; }
  .contact--phone { left: 17px; top: 381px; }
  .contact--email { left: 17px; top: 402px; }
  .contact--social { right: 15px; top: 402px; }
  .social-dot {
    width: 13px; height: 13px;
    border: 1.5px solid var(--text-light);
    border-radius: 50%;
  }
  .services {
    position: absolute;
    list-style: none;
    font-size: 19px;
    line-height: 1;
  }
  .services li {
    display: flex;
    align-items: center;
    gap: 4px;
    height: 35.3px;
  }
  .services svg { width: 14px; height: 14px; flex: none; }
  .services--left { left: 48px; top: 246px; }
  .services--right { left: 339px; top: 246px; }
</style>
</head>
<body>

<section class="card card--front" aria-label="Business card front">
  <div class="steel-panel"></div>
  <svg class="frame" viewBox="0 0 679 440" aria-hidden="true">
    <line x1="9" y1="9.5" x2="496" y2="9.5"/>
    <line x1="9.5" y1="9" x2="9.5" y2="135"/>
    <line x1="669.5" y1="305" x2="669.5" y2="431"/>
    <line x1="183" y1="430.5" x2="670" y2="430.5"/>
  </svg>
  <div class="wordmark wordmark-initials">RK</div>
  <div class="wordmark wordmark-name">IRONCRAFT</div>

  <div class="contact contact--phone">
    <svg viewBox="0 0 24 24" aria-hidden="true"><path fill="#e4e4e4" d="M6.6 10.8a15.1 15.1 0 0 0 6.6 6.6l2.2-2.2c.3-.3.7-.4 1-.2 1.1.4 2.3.6 3.6.6.6 0 1 .4 1 1V20c0 .6-.4 1-1 1A17 17 0 0 1 3 4c0-.6.4-1 1-1h3.5c.6 0 1 .4 1 1 0 1.3.2 2.5.6 3.6.1.3 0 .7-.2 1z"/></svg>
    <span>416-555-0193</span>
  </div>
  <div class="contact contact--email">
    <svg viewBox="0 0 24 24" aria-hidden="true"><rect x="2.5" y="5" width="19" height="14" rx="1.5" fill="none" stroke="#e4e4e4" stroke-width="1.8"/><path d="M3 6l9 7 9-7" fill="none" stroke="#e4e4e4" stroke-width="1.8"/></svg>
    <span>rk.ironcraftt@veltrano.com</span>
  </div>
  <div class="contact contact--social">
    <span class="social-dot" aria-hidden="true"></span>
    <span>@rk_ironcraft_</span>
  </div>
</section>

<section class="card card--back" aria-label="Business card back">
  <div class="steel-panel"></div>
  <svg class="frame" viewBox="0 0 679 440" aria-hidden="true">
    <line x1="9" y1="9.5" x2="496" y2="9.5"/>
    <line x1="9.5" y1="9" x2="9.5" y2="135"/>
    <line x1="669.5" y1="305" x2="669.5" y2="431"/>
    <line x1="183" y1="430.5" x2="670" y2="430.5"/>
  </svg>
  <div class="wordmark wordmark-initials">RK</div>
  <div class="wordmark wordmark-name">IRONCRAFT</div>

  <ul class="services services--left">
    <li><svg viewBox="0 0 14 14" aria-hidden="true"><path d="M2 12L12 2M8 2h4v4" fill="none" stroke="#e4e4e4" stroke-width="1.3"/></svg>Siding</li>
    <li><svg viewBox="0 0 14 14" aria-hidden="true"><path d="M2 12L12 2M8 2h4v4" fill="none" stroke="#e4e4e4" stroke-width="1.3"/></svg>ACM Panels</li>
    <li><svg viewBox="0 0 14 14" aria-hidden="true"><path d="M2 12L12 2M8 2h4v4" fill="none" stroke="#e4e4e4" stroke-width="1.3"/></svg>Standing Seam</li>
    <li><svg viewBox="0 0 14 14" aria-hidden="true"><path d="M2 12L12 2M8 2h4v4" fill="none" stroke="#e4e4e4" stroke-width="1.3"/></svg>Soffit</li>
    <li><svg viewBox="0 0 14 14" aria-hidden="true"><path d="M2 12L12 2M8 2h4v4" fill="none" stroke="#e4e4e4" stroke-width="1.3"/></svg>Fascia</li>
  </ul>
  <ul class="services services--right">
    <li><svg viewBox="0 0 14 14" aria-hidden="true"><path d="M2 12L12 2M8 2h4v4" fill="none" stroke="#e4e4e4" stroke-width="1.3"/></svg>Gutters</li>
    <li><svg viewBox="0 0 14 14" aria-hidden="true"><path d="M2 12L12 2M8 2h4v4" fill="none" stroke="#e4e4e4" stroke-width="1.3"/></svg>Metal</li>
    <li><svg viewBox="0 0 14 14" aria-hidden="true"><path d="M2 12L12 2M8 2h4v4" fill="none" stroke="#e4e4e4" stroke-width="1.3"/></svg>Aluminum</li>
    <li><svg viewBox="0 0 14 14" aria-hidden="true"><path d="M2 12L12 2M8 2h4v4" fill="none" stroke="#e4e4e4" stroke-width="1.3"/></svg>Vinyl</li>
    <li><svg viewBox="0 0 14 14" aria-hidden="true"><path d="M2 12L12 2M8 2h4v4" fill="none" stroke="#e4e4e4" stroke-width="1.3"/></svg>Metal Roofs and Roof Repairs</li>
  </ul>
</section>

</body>
</html>
```